Elementary School Yearbook Cover

We need a cover/back cover design for our elementary school yearbook . I attached a couple of samples that my yearbook team would like the direction of our cover to lean towards.

Front Cover:
School Name: Milton Varosky Elementary School
Mascot: Stormfoxes
Yearbook Motto for Front Cover: Leave a Legacy
Years to be printed: 2019-2020
School Colors: Red, White, Black, Gold (All four colors do not have to be utilized. )

Back Cover: 15 years of Excellence

Cover Dimensions
We are designing for an 8 1/2' x 11' book with 90 pages. No spine annotation required. Some parents have upgraded to a hardcover book so please keep all text in the softcover snap lines. Below is the website with specifications.
https://plumbook.helpdeskly.example/hc/en-us/articles/300061682-PB7-Cover-Page-Spread-Size-Dimensions-and-Resolution-Specifications

School Website: https://pages.kbvsd.example/varosky/
The mascot on the website is outdated. We hope a new and fresh version can be utilized for our cover.

```html
<!DOCTYPE html>
<html lang="en">
<head>
<meta charset="utf-8">
<title>Milton Varosky Elementary School Yearbook 2019-2020 Cover</title>
<link rel="stylesheet" href="https://fonts.googleapis.com/css2?family=Abril+Fatface&family=Cormorant+Garamond:wght@500&family=Great+Vibes&family=Playfair+Display+SC:wght@900&display=swap">
<style>
  :root {
    --backdrop: #dde7e6;
    --red-top: #ec1c24;
    --red-mid: #b80f15;
    --red-bottom: #780000;
    --red-deep: #5e0000;
    --white: #ffffff;
    --ember: #d42a12;
    --shadow: rgba(40, 0, 0, 0.35);
  }
  * { box-sizing: border-box; margin: 0; padding: 0; }
  html, body {
    width: 1200px;
    height: 900px;
    overflow: hidden;
    background: var(--backdrop);
  }
  .canvas {
    position: relative;
    width: 1200px;
    height: 900px;
  }
  .cover {
    position: absolute;
    top: 100px;
    width: 541px;
    height: 700px;
    color: var(--white);
    box-shadow: 0 10px 30px var(--shadow);
    overflow: hidden;
  }
  .cover--front {
    left: 39px;
    background: linear-gradient(180deg, var(--red-top) 0%, var(--red-mid) 45%, var(--red-bottom) 100%);
  }
  .cover--back {
    left: 620px;
    background: linear-gradient(180deg, var(--red-top) 0%, var(--red-mid) 35%, var(--red-deep) 100%);
  }
  .school-title {
    position: absolute;
    top: 72px;
    left: 20px;
  }
  .school-title__name {
    font-family: "Cormorant Garamond", serif;
    font-weight: 500;
    font-size: 29px;
    line-height: 1;
    text-transform: uppercase;
    letter-spacing: 0.01em;
  }
  .school-title__type {
    font-family: "Cormorant Garamond", serif;
    font-weight: 500;
    font-size: 18px;
    line-height: 1.2;
    text-transform: uppercase;
    letter-spacing: 0.1em;
    margin-top: 2px;
  }
  .school-title__years {
    font-family: "Abril Fatface", serif;
    font-size: 42px;
    line-height: 1.1;
    margin-top: 6px;
  }
  .mascot-art {
    position: absolute;
    top: 222px;
    left: 24px;
    width: 500px;
    height: 330px;
    border-radius: 45% 55% 40% 60% / 55% 45% 55% 45%;
    background: radial-gradient(ellipse at 40% 60%, var(--ember) 0%, rgba(150, 10, 10, 0.6) 55%, rgba(120, 0, 0, 0) 78%);
  }
  .motto {
    position: absolute;
    top: 565px;
    left: 0;
    width: 100%;
    text-align: center;
    font-family: "Great Vibes", cursive;
    font-size: 64px;
    line-height: 1;
  }
  .back-heading {
    position: absolute;
    top: 100px;
    left: 40px;
    font-family: "Playfair Display SC", serif;
    font-weight: 900;
    font-size: 38px;
    line-height: 1.15;
    text-transform: uppercase;
    letter-spacing: 0.01em;
  }
  .back-heading__small {
    font-size: 28px;
  }
</style>
</head>
<body>
  <main class="canvas">
    <section class="cover cover--front" aria-label="Front cover">
      <header class="school-title">
        <p class="school-title__name">Milton Varosky</p>
        <p class="school-title__type">Elementary School</p>
        <p class="school-title__years">2019-2020</p>
      </header>
      <div class="mascot-art" role="img" aria-label="Stormfoxes mascot illustration in red and orange with black outlines, swooping with wings raised"></div>
      <p class="motto">Leave a Legacy</p>
    </section>

    <section class="cover cover--back" aria-label="Back cover">
      <h2 class="back-heading">
        15 Years <span class="back-heading__small">of</span><br>Excellence
      </h2>
    </section>
  </main>
</body>
</html>
```